依頼詳細
大通りに面していて車で走りながら見てすぐにわかるように、かつ目を引く看板のデザインがいいです。ターゲット層は20才から年配の方までは幅広いですがシンプルで温かみがありわかりやすいデザインを希望します。
記載項目
サイズ:横100cm×縦420cm
建物全体の色が白系統となります。「ギフト専門店」「贈答品専門店」「贈答品」「ギフト」などの何のお店なのか分かる必要があります。また、結婚内祝・出産内祝・景品・香典返しの文言を組み込んで欲しいです。
希望イメージ
シンプル 複雑
単色 カラフル
暗い 明るい
日常 高級
遊び心 厳粛
未来的 伝統的
女性的 男性的
希望する色
特にないですが、店舗全体の色が白系統です。
納品ファイル
• イラストレーター形式 (.ai)
補足説明
イメージデータはハコブネ転送にアップロードしました。
https://73.hakobune-sd.jp/0528-c3d1e8a0f4b72a903e1c5d6084b2f7e6
現在の外観写真を添付します。

シンプルですが、伝えたいことが分かる視認性を重視しました。

この度はコンペ参加ありがとうございます。今後ともよろしくお願いします。

```html
<!DOCTYPE html>
<html lang="ja">
<head>
<meta charset="utf-8">
<title>贈答品専門店 看板</title>
<link rel="stylesheet" href="https://fonts.googleapis.com/css2?family=M+PLUS+Rounded+1c:wght@700;800&display=swap">
<style>
  :root{
    --paper:#ffffff;
    --navy:#1f3a6b;
    --ribbon:#e5486f;
    --ribbon-fold:#c93a5e;
    --pink:#ea6d97;
    --orange:#f3992a;
    --green:#8dc045;
    --purple:#b15fa6;
    --white:#ffffff;
  }
  html,body{margin:0;padding:0;width:1200px;height:5032px;overflow:hidden;background:var(--paper);}
  .sign{position:relative;width:1200px;height:5032px;}
  .sign svg{display:block;}
  .title-text{font-family:"M PLUS Rounded 1c",sans-serif;font-weight:800;fill:var(--navy);}
  .ribbon-text{font-family:"M PLUS Rounded 1c",sans-serif;font-weight:800;fill:var(--white);}
  .badge-text{font-family:"M PLUS Rounded 1c",sans-serif;font-weight:700;fill:var(--white);}
  .badge-shape{mix-blend-mode:multiply;}
</style>
</head>
<body>
<main class="sign">
<svg width="1200" height="5032" viewBox="0 0 1200 5032" xmlns="http://www.w3.org/2000/svg">
  <defs>
    <radialGradient id="wreathTone" cx="50%" cy="50%" r="50%">
      <stop offset="55%" stop-color="#ffffff" stop-opacity="0"/>
      <stop offset="80%" stop-color="#f7cfd8"/>
      <stop offset="100%" stop-color="#cfe0f2" stop-opacity="0.6"/>
    </radialGradient>
    <linearGradient id="meadowTone" x1="0" y1="0" x2="0" y2="1">
      <stop offset="0%" stop-color="#ffffff" stop-opacity="0"/>
      <stop offset="35%" stop-color="#f8dbe3"/>
      <stop offset="100%" stop-color="#d7e6f3"/>
    </linearGradient>
    <g id="scallop">
      <circle r="395"/>
      <circle cy="-275" r="155"/>
      <circle cy="-275" r="155" transform="rotate(36)"/>
      <circle cy="-275" r="155" transform="rotate(72)"/>
      <circle cy="-275" r="155" transform="rotate(108)"/>
      <circle cy="-275" r="155" transform="rotate(144)"/>
      <circle cy="-275" r="155" transform="rotate(180)"/>
      <circle cy="-275" r="155" transform="rotate(216)"/>
      <circle cy="-275" r="155" transform="rotate(252)"/>
      <circle cy="-275" r="155" transform="rotate(288)"/>
      <circle cy="-275" r="155" transform="rotate(324)"/>
    </g>
    <path id="sparkle" d="M0 -16 L4 -4 L16 0 L4 4 L0 16 L-4 4 L-16 0 L-4 -4 Z"/>
  </defs>

  <!-- header wreath -->
  <ellipse class="wreath" role="img" aria-label="パステルカラーの花と葉のリース" cx="600" cy="560" rx="580" ry="520" fill="url(#wreathTone)"/>

  <!-- footer flowers (behind badges) -->
  <rect class="meadow" role="img" aria-label="パステルカラーの花が並ぶ足元の飾り" x="0" y="4520" width="1200" height="512" fill="url(#meadowTone)"/>

  <!-- ribbon -->
  <g class="ribbon">
    <path d="M150 250 L250 250 L250 380 L150 380 L195 315 Z" fill="var(--ribbon-fold)"/>
    <path d="M1050 250 L950 250 L950 380 L1050 380 L1005 315 Z" fill="var(--ribbon-fold)"/>
    <path d="M220 225 Q600 195 980 225 L980 365 Q600 335 220 365 Z" fill="var(--ribbon)"/>
    <text class="ribbon-text" x="600" y="325" font-size="104" text-anchor="middle">真心を伝える</text>
  </g>

  <!-- shop title -->
  <text class="title-text" x="600" y="610" font-size="190" text-anchor="middle">贈答品</text>
  <text class="title-text" x="600" y="830" font-size="190" text-anchor="middle">専門店</text>

  <!-- dotted rings -->
  <g class="rings" fill="none" stroke-width="8" stroke-linecap="round" stroke-dasharray="0 22">
    <circle cx="600" cy="1640" r="490" stroke="var(--pink)"/>
    <circle cx="600" cy="2460" r="490" stroke="var(--orange)"/>
    <circle cx="600" cy="3280" r="490" stroke="var(--green)"/>
    <circle cx="600" cy="4100" r="490" stroke="var(--purple)"/>
  </g>
  <g class="sparkles">
    <use href="#sparkle" x="95" y="1670" fill="var(--pink)"/>
    <use href="#sparkle" x="1105" y="1670" fill="var(--pink)"/>
    <use href="#sparkle" x="95" y="2490" fill="var(--orange)"/>
    <use href="#sparkle" x="1105" y="2490" fill="var(--orange)"/>
    <use href="#sparkle" x="95" y="3310" fill="var(--green)"/>
    <use href="#sparkle" x="1105" y="3310" fill="var(--green)"/>
    <use href="#sparkle" x="95" y="4130" fill="var(--purple)"/>
    <use href="#sparkle" x="1105" y="4130" fill="var(--purple)"/>
  </g>

  <!-- category badges -->
  <g class="badges">
    <g class="badge-shape" fill="var(--pink)"><use href="#scallop" x="600" y="1640"/></g>
    <g class="badge-shape" fill="var(--orange)"><use href="#scallop" x="600" y="2460"/></g>
    <g class="badge-shape" fill="var(--green)"><use href="#scallop" x="600" y="3280"/></g>
    <g class="badge-shape" fill="var(--purple)"><use href="#scallop" x="600" y="4100"/></g>
  </g>

  <g class="badge-labels" text-anchor="middle" font-size="220">
    <text class="badge-text" x="600" y="1615">結婚</text>
    <text class="badge-text" x="600" y="1840">内祝</text>
    <text class="badge-text" x="600" y="2435">出産</text>
    <text class="badge-text" x="600" y="2660">内祝</text>
    <text class="badge-text" x="600" y="3255">祝賀</text>
    <text class="badge-text" x="600" y="3480">景品</text>
    <text class="badge-text" x="600" y="4075">香典</text>
    <text class="badge-text" x="600" y="4300">返し</text>
  </g>
</svg>
</main>
</body>
</html>
```